Business Card Design for Retail Product Line

We need a two-sided, full-color business card for a new oral care product line. The feel of the card should invoke emotions of happiness and health. It should be bright, cheerful and modern in appearance. The card should be mostly matte finish, but with elements of spot-gloss and/or raised/embossed features (print, logo, tag lines, etc.).

Target Market(s)

People who are into whole-body health, eat well and understand the importance of nutrition.

Industry/Entity Type

Health And Wellness

Contact Information for Business Card

The logo, color scheme and tag-lines have all been developed and artwork is attached. Card is to be standard-sized and should use a mix of clean, sans-serif fonts; the main font (DIN) is attached as well. The card will be used for 3 individuals and should include placeholders for:
1. Name
2. Title (for example, "CEO")
3. Business address
4. Phone number
5. Website
6. Email address

Font styles to use
Sans Serif
Other font styles liked:
• DIN font

Colors
faa54b
000000
5c5c5c
a2ce44

Requirements
Must have
• 2 sides
• Full color orange on one side
• Image of DNA leaves
• Tag line "Glow from the Root Upward", on single side with orange background
• Company Logo (Plome) on same side as text (name, phone, address, etc.)
• Name, Title, Business Address, Phone Number, Website, Email address
• UPDATE: "Brisk Marrow", not "Brisk M Arrow"
Should not have
• Calligraphy
• Dark colors
• UPDATE!! Do not include "Turmeric infused toothpaste" on the business card
• UPDATE #2!! Do not include "Brisk Marrow" on the business card

```html
<!DOCTYPE html>
<html lang="en">
<head>
<meta charset="utf-8">
<title>Plome Business Card</title>
<link rel="stylesheet" href="https://fonts.googleapis.com/css2?family=Barlow:wght@400;500;600;700&display=swap">
<style>
  :root {
    --orange: #faa54b;
    --orange-deep: #f0a030;
    --gold: #f3cf4a;
    --green: #3a9a3c;
    --green-light: #a2ce44;
    --grey: #5c5c5c;
    --black: #000000;
    --white: #ffffff;
    --stage: #d9d9d9;
  }
  * { box-sizing: border-box; margin: 0; padding: 0; }
  html, body { width: 1200px; height: 843px; overflow: hidden; }
  body {
    background: var(--stage);
    font-family: "Barlow", sans-serif;
    position: relative;
  }
  .card {
    position: absolute;
    width: 620px;
    height: 354px;
    overflow: hidden;
    box-shadow: 0 6px 18px rgba(0,0,0,0.18);
  }

  /* Back side */
  .card-back { left: 110px; top: 100px; background: var(--white); }
  .claim-bar {
    position: absolute; left: 122px; top: 202px;
    width: 130px; height: 12px; background: var(--grey);
    color: var(--white); font-size: 8px; letter-spacing: 1px;
    line-height: 12px; padding-left: 8px; text-transform: uppercase;
  }
  .dna-leaves {
    position: absolute; left: 468px; top: 30px;
    width: 110px; height: 210px; border-radius: 40px;
    background: linear-gradient(180deg, var(--green-light) 0%, #8bbd3a 30%, #b5b5b5 55%, var(--green) 100%);
  }

  /* Front side */
  .card-front { left: 460px; top: 390px; }
  .card-front .face { position: absolute; inset: 0; }
  .tagline {
    position: absolute; left: 36px; top: 34px;
    color: var(--white); text-transform: uppercase;
    font-weight: 700; font-size: 14px; line-height: 1.05;
  }
  .tagline .lead { display: block; font-size: 34px; text-transform: lowercase; line-height: 0.95; }
  .contact {
    position: absolute; left: 36px; top: 140px;
    list-style: none; color: var(--white);
    font-size: 14px; line-height: 20px;
  }
  .contact li { display: flex; align-items: center; gap: 10px; white-space: nowrap; }
  .contact .icon { width: 14px; height: 14px; flex: none; }
  .contact .address { padding-left: 24px; }
  .person {
    position: absolute; right: 40px; top: 74px; text-align: right;
    text-transform: uppercase;
  }
  .person .name { color: var(--grey); font-size: 19px; font-weight: 700; letter-spacing: 0.5px; }
  .person .role { color: var(--grey); font-size: 14px; letter-spacing: 1px; }
  .company-name {
    position: absolute; right: 70px; bottom: 44px;
    color: var(--white); font-size: 78px; font-weight: 600;
    line-height: 1; letter-spacing: 1px;
  }
</style>
</head>
<body>

  <section class="card card-back" aria-label="Card back">
    <div class="claim-bar">Nature + Science</div>
    <div class="dna-leaves" role="img" aria-label="Illustration of a DNA helix topped with green leaves"></div>
  </section>

  <section class="card card-front" aria-label="Card front">
    <svg class="face" viewBox="0 0 620 354" width="620" height="354" aria-hidden="true">
      <defs>
        <linearGradient id="orangeFill" x1="0" y1="0" x2="1" y2="0.6">
          <stop offset="0" stop-color="var(--orange-deep)"/>
          <stop offset="0.55" stop-color="var(--orange)"/>
          <stop offset="1" stop-color="var(--gold)"/>
        </linearGradient>
      </defs>
      <rect width="620" height="354" fill="url(#orangeFill)"/>
      <path d="M220 0 C400 36 560 120 620 262 V0 Z" fill="var(--white)"/>
      <path d="M250 0 C420 34 570 112 620 224" fill="none" stroke="var(--orange)" stroke-width="2"/>
      <circle cx="262" cy="10" r="8" fill="var(--white)"/>
    </svg>

    <p class="tagline"><span class="lead">glow</span>from the<br>root upward™</p>

    <ul class="contact">
      <li class="address">2719 Alder Crest Lane</li>
      <li class="address">Ferndale Point, NY 10988</li>
      <li>
        <svg class="icon" viewBox="0 0 16 16"><path d="M3 6 C3 3 13 3 13 6 L11 7 9 5 H7 L5 7 Z M4 8 H12 V13 H4 Z" fill="var(--white)"/></svg>
        555 0142 7781
      </li>
      <li>
        <svg class="icon" viewBox="0 0 16 16"><rect x="1" y="3" width="14" height="10" fill="var(--white)"/><path d="M1 3 L8 9 L15 3" fill="none" stroke="var(--orange)" stroke-width="1.2"/></svg>
        mara@plome-care.com
      </li>
      <li>
        <svg class="icon" viewBox="0 0 16 16"><circle cx="8" cy="8" r="7" fill="var(--white)"/><path d="M1 8 H15 M8 1 C4 5 4 11 8 15 M8 1 C12 5 12 11 8 15" fill="none" stroke="var(--orange)" stroke-width="1"/></svg>
        www.plome-care.com
      </li>
    </ul>

    <div class="person">
      <p class="name">Mara Lindqvist</p>
      <p class="role">President</p>
    </div>

    <p class="company-name">plome</p>
  </section>

</body>
</html>
```